Interior Stylist business card design needed

I need a business card for my new company in Sydney called "Lu Brannigan Designs". The business offers an interior styling and colour consultancy. My clients are generally not very design savvy (hence why they use me) and can range from being quite conservative to really wanting something "out there". They can be looking for a budget makeover or something more expensive / substantial. I'd like my business card design to be stylish (but not overly formal). I certainly don't want it to be conservative. I'd like it to stand out a bit! I don't really have any aversion to particular colours and I don't have a logo as such - my business name is really all I have.

Target Market(s)

As above - home owners, ranging from conservative to modern

Industry/Entity Type

Conservative

Contact Information for Business Card

Lu Brannigan Designs
Colour consultancy and interior styling
ph: 0417 368 205
email: lubrannigan@zephmail.net.au

Requirements
Should not have
• Old fashioned writing or motifs. No Times Roman font!!

```html
<!DOCTYPE html>
<html lang="en">
<head>
<meta charset="utf-8">
<title>Lu Brannigan Designs – Business Card</title>
<link href="https://fonts.googleapis.com/css2?family=Lato:wght@300;400&display=swap" rel="stylesheet">
<style>
  :root {
    --stage: #33241a;
    --card-white: #ffffff;
    --orange: #f07a3e;
    --orange-deep: #e4692e;
    --blue: #29399a;
    --text-light: #ffffff;
    --radius: 22px;
  }
  html, body {
    margin: 0;
    width: 1200px;
    height: 750px;
    overflow: hidden;
    background: var(--stage);
    font-family: "Lato", sans-serif;
  }
  .stage {
    position: relative;
    width: 1200px;
    height: 750px;
  }
  .card {
    position: absolute;
    top: 205px;
    width: 540px;
    height: 340px;
    border-radius: var(--radius);
    overflow: hidden;
    box-shadow: 0 14px 30px rgba(0,0,0,0.45);
  }
  .card--front { left: 40px; background: var(--card-white); }
  .card--back  { left: 620px; background: var(--orange); }

  /* Front */
  .name-tab {
    position: absolute;
    top: 0;
    right: 0;
    width: 220px;
    height: 36px;
  }
  .name-tab svg { position: absolute; inset: 0; }
  .name-tab__text {
    position: relative;
    display: block;
    padding-left: 58px;
    line-height: 36px;
    color: var(--text-light);
    font-size: 15px;
    letter-spacing: 0.5px;
    text-transform: uppercase;
  }
  .chair-pattern {
    position: absolute;
    background: linear-gradient(180deg, var(--orange) 0%, var(--orange-deep) 100%);
  }
  .card--front .chair-pattern {
    left: 0; right: 0;
    top: 80px;
    height: 176px;
  }
  .tagline-band {
    position: absolute;
    left: 0; right: 0;
    top: 256px;
    height: 26px;
    background: var(--blue);
    color: var(--text-light);
    font-size: 14.5px;
    line-height: 26px;
    text-align: center;
    text-transform: uppercase;
    letter-spacing: 0.3px;
    white-space: nowrap;
  }

  /* Back */
  .card--back .chair-pattern { inset: 0; }
  .business-name {
    position: absolute;
    left: 40px;
    right: 30px;
    top: 92px;
    margin: 0;
    color: var(--text-light);
    font-weight: 300;
    font-size: 38px;
    letter-spacing: 1px;
    text-transform: uppercase;
    text-align: right;
    line-height: 1.1;
  }
  .contact {
    position: absolute;
    right: 28px;
    bottom: 26px;
    margin: 0;
    color: var(--text-light);
    font-weight: 300;
    font-size: 12px;
    line-height: 1.7;
    text-align: right;
    font-style: normal;
    opacity: 0.92;
  }
</style>
</head>
<body>
<main class="stage">
  <section class="card card--front" aria-label="Business card front">
    <div class="name-tab">
      <svg width="220" height="36" viewBox="0 0 220 36" aria-hidden="true">
        <path d="M0 0 H220 V36 H30 Z" fill="var(--blue)"/>
      </svg>
      <span class="name-tab__text">Lu Brannigan</span>
    </div>
    <div class="chair-pattern" role="img" aria-label="Faint line drawings of chairs and sofas on orange"></div>
    <div class="tagline-band">Lu Brannigan Designs Colour Consultancy and Interior Styling</div>
  </section>

  <section class="card card--back" aria-label="Business card back">
    <div class="chair-pattern" role="img" aria-label="Faint line drawings of chairs and sofas on orange"></div>
    <h1 class="business-name">Lu Brannigan Designs</h1>
    <address class="contact">
      Call 0417 368 205<br>
      lubrannigan@zephmail.net.au
    </address>
  </section>
</main>
</body>
</html>
```